Business card design and logo needed

We have been operating as Ridgeline Posts for 30 years but never had a logo and feel there is a need for one, but have no idea for a design.
We specialise in all types of rural fencing including post and wire, post and rail, electric, chainmesh and to a lesser extent, also do industrial security fencing.
Updates

Sorry, but website is ridgelineposts.example

No .au on the end!
My apologies

Regards, Darren

Target Market(s)

Rural/acreage property owners, particularly horse people.

Industry/Entity Type

Industrial

Contact Information for Business Card

Ridgeline Posts Darren Kellett 0499 572106. Lewis Kellett 0499 613720
Email: ridgelineposts@mailhub.example
Website: www.ridgelineposts.example.au

Requirements
Must have
• Would like to highlight website address - use the business card to advertise the website or to push them to check it out.

```html
<!DOCTYPE html>
<html lang="en">
<head>
<meta charset="utf-8">
<title>Ridgeline Posts – Business Card</title>
<link rel="stylesheet" href="https://fonts.googleapis.com/css2?family=Open+Sans:wght@400;700&display=swap">
<style>
  :root {
    --page-bg: #2a2e30;
    --card-dark: #16181a;
    --card-mid: #1d201f;
    --card-top: #1a211c;
    --band-line: #3c423d;
    --text-light: #d9dbdc;
    --text-soft: #a9adaf;
    --accent: #d9772a;
  }
  * { margin: 0; padding: 0; box-sizing: border-box; }
  html, body {
    width: 1200px; height: 741px; overflow: hidden;
    background: var(--page-bg);
    font-family: "Open Sans", Verdana, sans-serif;
  }
  .sheet {
    position: relative; width: 1200px; height: 741px;
    display: flex; flex-direction: column; align-items: center; justify-content: center; gap: 26px;
  }
  .card {
    position: relative; width: 600px; height: 343px; overflow: hidden;
    box-shadow: 0 10px 30px rgba(0,0,0,.45);
  }
  .card-front {
    background: linear-gradient(160deg, var(--card-mid), var(--card-dark));
  }
  .front-band { position: absolute; inset: 0; width: 100%; height: 100%; }
  .brand {
    position: absolute; top: 62px; left: 0; right: 0;
    display: flex; align-items: center; justify-content: center; gap: 12px;
  }
  .brand-mark { width: 14px; height: 14px; background: var(--text-soft); }
  .brand-name { font-size: 26px; font-weight: 400; color: var(--text-soft); letter-spacing: .5px; white-space: nowrap; }
  .contacts {
    position: absolute; top: 192px; left: 0; right: 0;
    display: flex; justify-content: center; align-items: flex-start;
  }
  .person { width: 220px; white-space: nowrap; }
  .person-left { text-align: right; padding-right: 26px; }
  .person-right { text-align: left; padding-left: 26px; }
  .divider { width: 1px; height: 50px; background: var(--text-soft); }
  .person-name { font-size: 19px; font-weight: 700; color: var(--text-light); line-height: 1.2; }
  .person-phone {
    font-size: 12px; color: var(--text-soft); margin-top: 2px;
    display: inline-flex; align-items: center; gap: 6px;
  }
  .icon { width: 12px; height: 12px; fill: none; stroke: var(--text-soft); stroke-width: 1.3; flex: none; }
  .icon-solid { fill: var(--text-soft); stroke: none; }
  .details {
    position: absolute; top: 268px; left: 200px;
    display: flex; flex-direction: column; gap: 6px; font-size: 12.5px; white-space: nowrap;
  }
  .detail { display: flex; align-items: center; gap: 12px; color: var(--text-light); }
  .detail-web { color: var(--accent); }
  .card-back { background: linear-gradient(160deg, #1b1c1d, #0f1011); display: flex; align-items: center; justify-content: center; }
  .back-web { color: var(--accent); font-size: 14px; letter-spacing: 1.5px; white-space: nowrap; }
</style>
</head>
<body>
<main class="sheet">
  <section class="card card-front" aria-label="Business card front">
    <svg class="front-band" viewBox="0 0 600 343" preserveAspectRatio="none" aria-hidden="true">
      <path d="M0 0 H600 V0 C520 140 330 172 0 160 Z" fill="var(--card-top)"/>
      <path d="M0 160 C330 172 520 140 600 0" fill="none" stroke="var(--band-line)" stroke-width="2"/>
    </svg>
    <div class="brand">
      <span class="brand-mark"></span>
      <span class="brand-name">Ridgeline Posts</span>
    </div>
    <div class="contacts">
      <div class="person person-left">
        <div class="person-name">Darren Kellett</div>
        <div class="person-phone">
          <svg class="icon" viewBox="0 0 12 12"><path class="icon-solid" d="M1 4 Q6 0 11 4 L10 6 L8 5 V4 H4 V5 L2 6 Z M3 7 H9 L10 11 H2 Z"/></svg>
          0499 572106
        </div>
      </div>
      <div class="divider"></div>
      <div class="person person-right">
        <div class="person-name">Lewis Kellett</div>
        <div class="person-phone">
          <svg class="icon" viewBox="0 0 12 12"><path class="icon-solid" d="M1 4 Q6 0 11 4 L10 6 L8 5 V4 H4 V5 L2 6 Z M3 7 H9 L10 11 H2 Z"/></svg>
          0499 613720
        </div>
      </div>
    </div>
    <div class="details">
      <div class="detail">
        <svg class="icon" viewBox="0 0 12 12"><rect x="1" y="2.5" width="10" height="7"/><path d="M1 2.5 L6 7 L11 2.5"/></svg>
        ridgelineposts@mailhub.example
      </div>
      <div class="detail detail-web">
        <svg class="icon" viewBox="0 0 12 12"><circle cx="6" cy="6" r="5"/><ellipse cx="6" cy="6" rx="2.2" ry="5"/><path d="M1 6 H11"/></svg>
        www.ridgelineposts.example
      </div>
    </div>
  </section>
  <section class="card card-back" aria-label="Business card back">
    <span class="back-web">www.ridgelineposts.example</span>
  </section>
</main>
</body>
</html>
```